Social media design templates

A variety of templates incorporating our logo and colours to use for our postings on different social media platforms. Must be user friendly and meet our brand image. We have attached our logo to view. We would like some of the templates to offer the ability to insert a background image and others to be a template designed around our logo.

We are black and white in colour, and our values speak to our transparency and honesty, so we are looking for clean cut, sharp straight lines, not using any other colours or curved lines.

We are a recruitment company that will be using these templates
- job posting,
- general announcements,
- blog,
- company newsletter,
- updates,
- testimonials and
- top candidate profiles

We would like a gallery of templates to choose from to use separately that all represent our brand.

```html
<!DOCTYPE html>
<html lang="en">
<head>
<meta charset="utf-8">
<title>Talent Bridge Group – Social Templates</title>
<link href="https://fonts.googleapis.com/css2?family=Oswald:wght@400;500;700&family=Montserrat:wght@500;700;800&display=swap" rel="stylesheet">
<style>
  :root{
    --board:#e4e4e4;
    --ink:#111111;
    --white:#ffffff;
    --paper:#f3f3f3;
    --grey:#8c8c8c;
    --grey-light:#d8d8d8;
    --dark:#232323;
    --index:#a9a9a9;
  }
  *{margin:0;padding:0;box-sizing:border-box}
  html,body{width:795px;height:1200px;overflow:hidden}
  body{background:var(--board);position:relative;font-family:"Montserrat",sans-serif}

  .template{position:absolute;left:127px;width:541px;height:541px;overflow:hidden;box-shadow:0 6px 18px rgba(0,0,0,.28)}
  .template--job{top:40px;background:var(--paper)}
  .template--announce{top:618px;background:var(--dark)}
  .template-index{position:absolute;left:700px;font-family:"Oswald",sans-serif;font-weight:500;font-size:64px;color:var(--index)}
  .template-index--one{top:228px}
  .template-index--two{top:830px}

  .brand{position:absolute;left:30px;top:22px;width:130px;padding:14px 8px;border:2px solid currentColor;text-align:center;font-family:"Oswald",sans-serif;font-weight:500;font-size:17px;line-height:1.2;letter-spacing:1px;text-transform:uppercase}
  .template--job .brand{color:var(--ink);background:var(--white)}
  .template--announce .brand{color:var(--white)}

  .decor{position:absolute;inset:0;width:541px;height:541px}

  .hiring{position:absolute;left:24px;top:196px;display:flex;align-items:center;gap:6px}
  .hiring__horn{width:58px;height:52px;background:linear-gradient(135deg,#3a3a3a,#0d0d0d);border-radius:6px}
  .hiring__bubble{background:var(--ink);color:var(--white);font-family:"Oswald",sans-serif;font-weight:700;font-size:22px;line-height:1;padding:10px 14px;border-radius:8px;text-transform:uppercase;text-align:center}

  .job-title{position:absolute;left:30px;top:292px;font-family:"Oswald",sans-serif;font-weight:700;font-size:56px;line-height:.98;color:var(--ink);text-transform:uppercase}
  .skills{position:absolute;left:30px;top:418px;width:200px;color:var(--ink)}
  .skills__heading{font-family:"Oswald",sans-serif;font-weight:700;font-size:19px;text-transform:uppercase;margin-bottom:6px}
  .skills__list{list-style:none;font-weight:700;font-size:10px;line-height:1.3;text-transform:uppercase}
  .skills__list li{margin-bottom:4px;padding-left:10px;position:relative}
  .skills__list li::before{content:"•";position:absolute;left:0}

  .web-bar{position:absolute;left:355px;top:505px;width:186px;height:30px;background:var(--ink);color:var(--white);font-size:11px;font-weight:700;display:flex;align-items:center;justify-content:center;gap:8px}
  .web-bar__dot{width:10px;height:10px;background:var(--white)}

  .hex-title{position:absolute;left:175px;top:225px;width:295px;text-align:center;font-family:"Oswald",sans-serif;font-weight:500;font-size:34px;line-height:1.1;color:var(--grey);text-transform:uppercase}
  .socials{position:absolute;right:18px;top:405px;display:flex;flex-direction:column;gap:9px}
  .socials span{width:18px;height:18px;border:1.5px solid var(--white);border-radius:50%}
  .footer-web{position:absolute;left:0;right:0;top:510px;text-align:center;color:var(--white);font-size:11px;font-weight:700;letter-spacing:.5px}
</style>
</head>
<body>

<section class="template template--job">
  <svg class="decor" viewBox="0 0 541 541" aria-hidden="false">
    <rect x="210" y="300" width="331" height="200" fill="url(#piecesTone)" role="img" aria-label="Photo of white figurines with one dark figure standing out"/>
    <circle cx="360" cy="8" r="60" fill="#151515"/>
    <circle cx="492" cy="160" r="160" fill="none" stroke="#222" stroke-width="2" stroke-dasharray="6 6"/>
    <circle cx="492" cy="160" r="145" fill="url(#searchTone)" role="img" aria-label="Photo of a hand holding a magnifier over a candidate profile icon"/>
    <circle cx="468" cy="300" r="66" fill="#151515"/>
    <defs>
      <linearGradient id="searchTone" x1="0" y1="0" x2="1" y2="1">
        <stop offset="0" stop-color="#6f7880"/>
        <stop offset="1" stop-color="#1d2328"/>
      </linearGradient>
      <linearGradient id="piecesTone" x1="0" y1="0" x2="0" y2="1">
        <stop offset="0" stop-color="#f3f3f3"/>
        <stop offset="1" stop-color="#c9c9c9"/>
      </linearGradient>
    </defs>
  </svg>
  <div class="brand">Talent Bridge<br>Group</div>
  <div class="hiring">
    <div class="hiring__horn" role="img" aria-label="Megaphone illustration"></div>
    <div class="hiring__bubble">We Are<br>Hiring!</div>
  </div>
  <h2 class="job-title">Job<br>Posting</h2>
  <div class="skills">
    <h3 class="skills__heading">Required Skills:</h3>
    <ul class="skills__list">
      <li>Fluency in English is mandatory</li>
      <li>Should be flexible with night shift (home drop available)</li>
      <li>Both fresher &amp; experienced can apply</li>
    </ul>
  </div>
  <div class="web-bar"><span class="web-bar__dot"></span>www.website.com</div>
</section>
<div class="template-index template-index--one">1</div>

<section class="template template--announce">
  <svg class="decor" viewBox="0 0 541 541">
    <rect width="541" height="541" fill="url(#keysTone)" role="img" aria-label="Dark photo of a keyboard with social icons"/>
    <polygon points="240,110 420,150 480,290 410,420 240,445 120,360 110,200" fill="#ececec" stroke="#ffffff" stroke-width="8"/>
    <rect x="40" y="340" width="170" height="140" fill="url(#hornTone)" role="img" aria-label="Illustration of a hand holding a megaphone"/>
    <defs>
      <linearGradient id="keysTone" x1="0" y1="0" x2="1" y2="1">
        <stop offset="0" stop-color="#3a3a3a"/>
        <stop offset="1" stop-color="#161616"/>
      </linearGradient>
      <linearGradient id="hornTone" x1="0" y1="0" x2="1" y2="1">
        <stop offset="0" stop-color="#5a5a5a"/>
        <stop offset="1" stop-color="#1a1a1a"/>
      </linearGradient>
    </defs>
  </svg>
  <div class="brand">Talent Bridge<br>Group</div>
  <h2 class="hex-title">General<br>Announcements</h2>
  <div class="socials"><span></span><span></span><span></span><span></span></div>
  <p class="footer-web">WWW.WEBSITE.COM</p>
</section>
<div class="template-index template-index--two">2</div>

</body>
</html>
```